Design music inspired artwork for Tunevale

Your job is to design/create artwork that captures how music makes people feel.

Tunevale is looking to engage their audience of 18-24 year-olds for whom music plays an important role in developing their identity, navigating life, and connecting with people around them.

Music is a short cut to our emotions. And, music has always been part of our social experience. Tunevale believes music helps people express how they’re #HereHumming, and that discovering and sharing music with friends makes our connection to each other richer.
Tunevale is creating a campaign that shares people's #HereHumming stories of connecting with each other through music, enabled by Tunevale. Our objective is to showcase playful - but honest - moments between people, and in doing so showcase how the platform enables discovery, sharing, and conversation through music.

Tunevale invites artists and designers to submit artwork that best captures how music makes people feel and brings them together.

Submissions must capture one or all of:
- The feeling of listening to music with friends, families, loved ones
- a first dance or first kiss
- friends or people connecting at a festival
- How music unites people from all cultures and backgrounds
- How music moves us
- A vision of what you hear and feel when listening to a song
- Communicating something when words are not enough

The goal of the winning submissions is to use them across Tunevale's channels, to inspire their audience to create and share music playlists and use the many features of the platform. They will also be showcased as part of an official Tunevale event.

Tunevale & Crafthive understand that artists will have their own interpretation of the brief so be sure to include a description with your submission and share the Tunevale song or playlist that inspired it so we can follow your creative process.
To be eligible for full prizing, please set up a Crafthive profile and upload your design via Crafthive:

https://www.crafthive-example.com/i/design-for-tunevale

The PixelGuild project has 3 places, and the Crafthive package is even bigger! One overall winner will receive:
- $2,500
- Exposure across Tunevale social channels
- Their work showcased as part of an exclusive event in London
- A Tunevale Plus Account for 12 months
- The opportunity to feature in a Tunevale paid media campaign and/or to have future work commissioned by Tunevale
- A minimum of 20 finalists will have their work showcased as part of an event – to be viewed by key senior figures within the creative, media and music industries.

Guidelines:
- Artists should retain their original artwork files (in 300dpi) but designs must be submitted in JPEG or PNG, max size 5MB
- All entries must be original artwork (meaning not using third party pre-existing copyright materials) - photographs will not be accepted.
- Artists must join Crafthive using an active email address in order to ensure they can be contacted should they be selected.

Judging panel:
MOIRA KELBECK (VP Creative and Brands Strategy at Tunevale)
DORIAN FALSTEDT (Director of Design, Communications at Tunevale)
RUPERT GADSBY (Executive Creative Director of independent, London ad agency Lantern and Quill)
OWEN MARCHE (Co-founder at Bright Odd Thing)

*NB: Please do not include logos or the hashtag on your artwork- these can be added to the winning design once it has been selected.

Incentives have been increased!  We look forward to seeing your submissions.

If anyone has any questions or issues with the brief, please do not hesitate to ask.

Target Market(s)

Target market:

18-24 year-olds for whom music plays an important role in developing their identity, navigating life, and connecting with people around them.

Industry/Entity Type

Ad Agency

Requirements
Must have
• - Designers are required to submit their design to Crafthive as well as PixelGuild (to be eligible for the Crafthive prize packages).
Nice to have
• - A full Crafthive profile to be reviewed by the judging panel (a very good way to get more of your work noticed by the panel of expert judges!)
Should not have
• - Profanities, illicit substances, anything offensive

```html
<!DOCTYPE html>
<html lang="en">
<head>
<meta charset="utf-8">
<title>Back to the root – Tunevale artwork</title>
<link rel="stylesheet" href="https://fonts.googleapis.com/css2?family=Roboto+Condensed:wght@300;700&display=swap">
<style>
  :root {
    --sky-yellow: #fbee9c;
    --pale-cream: #fffbe6;
    --petal-white: #fffaf0;
    --petal-gold: #f9d777;
    --bloom-orange: #f29433;
    --bloom-red: #e5201c;
    --ink: #111111;
  }
  * { margin: 0; padding: 0; box-sizing: border-box; }
  html, body {
    width: 1200px;
    height: 819px;
    overflow: hidden;
    background: var(--sky-yellow);
  }
  .poster {
    position: relative;
    width: 1200px;
    height: 819px;
    overflow: hidden;
    font-family: "Roboto Condensed", "Arial Narrow", sans-serif;
  }
  .bloom-artwork {
    position: absolute;
    inset: 0;
    background:
      radial-gradient(ellipse 190px 170px at 620px 640px, var(--bloom-red) 0%, var(--bloom-red) 45%, rgba(229,32,28,0) 100%),
      radial-gradient(ellipse 330px 260px at 620px 650px, var(--bloom-orange) 0%, var(--bloom-orange) 30%, rgba(242,148,51,0) 100%),
      radial-gradient(ellipse 260px 220px at 0px 819px, rgba(229,32,28,0.8) 0%, rgba(229,32,28,0) 100%),
      radial-gradient(ellipse 260px 220px at 1200px 819px, rgba(229,32,28,0.8) 0%, rgba(229,32,28,0) 100%),
      radial-gradient(ellipse 700px 420px at 610px 680px, var(--petal-gold) 0%, var(--petal-gold) 35%, rgba(249,215,119,0) 100%),
      radial-gradient(ellipse 900px 360px at 600px 520px, var(--petal-white) 0%, var(--petal-white) 50%, rgba(255,250,240,0) 100%),
      radial-gradient(ellipse 380px 200px at 1060px 200px, var(--pale-cream) 0%, rgba(255,251,230,0) 100%),
      linear-gradient(180deg, var(--sky-yellow) 0%, var(--sky-yellow) 25%, var(--pale-cream) 55%, var(--petal-white) 100%);
  }
  .headline {
    position: absolute;
    left: 52px;
    top: 158px;
    font-weight: 700;
    font-size: 118px;
    line-height: 1;
    letter-spacing: 2px;
    color: var(--ink);
    white-space: nowrap;
  }
  .tagline {
    position: absolute;
    left: 50px;
    top: 280px;
    font-weight: 300;
    font-size: 52px;
    line-height: 1;
    color: var(--ink);
    white-space: nowrap;
  }
</style>
</head>
<body>
  <main class="poster">
    <div class="bloom-artwork" role="img" aria-label="Sunlit close-up photograph filling the whole piece: a large blooming flower with cream and golden petals radiating from a bright red centre, against a pale yellow sky of soft white blossoms"></div>
    <h1 class="headline">Back to the root</h1>
    <p class="tagline">re-discover those lost moments</p>
  </main>
</body>
</html>
```